Verdant Crest 6x6m trade show booth, Wall Design

Project Overview:
Our technology company is preparing for an upcoming trade show where we will showcase various products and divisions, including thermal radars, sonar, rapid deployment solutions for perimeter security, a tactical trailer, drone technology, and our new and emerging technology division. We are seeking a graphic design for our trade show walls that will tie together all these elements while staying true to our brand identity.
Objectives:
Create a cohesive and visually appealing graphic design that integrates all elements of our trade show booth.
Emphasize our company's identity by featuring our logo and utilizing our brand colours.
Maintain a minimalistic design to ensure that our stand does not appear cluttered given the numerous elements on display.
Key Information:
Design Elements:
1. Logo Integration:
Place the company logo prominently on the trade show wall to establish brand presence.
2. Color Palette:
Use our brand colours throughout the design to maintain consistency and brand recognition.
3. Minimalistic Design:
Ensure that the design is clean and minimal to avoid overwhelming visitors with too much visual information.
4. Visual Hierarchy:
Organize the elements on the wall in a way that guides the viewer's eye naturally from one section to another.

The design should convey a sense of innovation, cutting-edge technology, and professionalism. It should inspire confidence in our products and services while being approachable.
Please feel free to ask for any additional information or clarification as needed. We are looking forward to a design that effectively represents our brand and products at the trade show. Thank you for your creative input and expertise in advance.
I have attached a detailed brief in the downloads with addition text and information to give further context to our company and also the event we will be attending.
Updates

After discussions with our team, they have decided to take a different approach and have on design replicated on both walls. this design will be one image across all panels with key words across the tob as well as our logo. please see updated design breif for details.

Target Market(s)

Professionals in Defence, Government and Critical Infrastructure

Industry/Entity Type

Defence, Government and Critical Infrastructure

Font styles to use
Sans Serif

Colors
0054AA
0677BA
7BADD7
CADEEF
E8F1F8

Requirements
Must have
• My project must have clear brand awareness and utilise the wall space provided with a cohesive design. The design must be in line with the artwork requirements provided in the downloadable brief.
Nice to have
• It would be nice to have a minimalist design while still standing out
Should not have
• No clutter, any information to be diplayed in a clean and consice manner.

```html
<!DOCTYPE html>
<html lang="en">
<head>
<meta charset="utf-8">
<title>Verdant Crest – Trade Show Wall</title>
<link rel="stylesheet" href="https://fonts.googleapis.com/css2?family=Lato:wght@900&family=Open+Sans:wght@400&display=swap">
<style>
  :root {
    --navy: #1b2350;
    --teal: #2a9fbf;
    --white: #ffffff;
    --sky-light: #d6e9f4;
    --sky: #a9d1ea;
    --sea-light: #3f7fbf;
    --sea: #1d5a9c;
    --sea-deep: #0e3a70;
    --sea-dark: #061a38;
    --backdrop-light: #b3b3b3;
    --backdrop-dark: #4a4a4a;
  }
  * { margin: 0; padding: 0; box-sizing: border-box; }
  html, body { width: 1200px; height: 465px; overflow: hidden; }
  body {
    background: linear-gradient(100deg, var(--backdrop-light) 0%, #9a9a9a 55%, var(--backdrop-dark) 100%);
    position: relative;
  }
  .wall {
    position: absolute;
    left: 46px;
    top: 36px;
    display: flex;
    gap: 20.5px;
  }
  .panel {
    width: 169px;
    height: 392px;
    display: flex;
    flex-direction: column;
    background: var(--white);
  }
  .panel-header {
    height: 99px;
    display: flex;
    align-items: center;
    justify-content: center;
    text-align: center;
  }
  .keyword {
    font-family: "Lato", sans-serif;
    font-weight: 900;
    font-size: 23px;
    line-height: 1.08;
    letter-spacing: -0.9px;
    color: var(--navy);
    text-transform: uppercase;
    margin-top: -14px;
  }
  .brand {
    display: flex;
    flex-direction: column;
    align-items: center;
    gap: 8px;
    margin-top: -6px;
  }
  .brand-mark {
    width: 40px;
    height: 40px;
    border-radius: 50%;
    background: var(--teal);
  }
  .brand-name {
    font-family: "Open Sans", sans-serif;
    font-weight: 400;
    font-size: 20px;
    color: var(--teal);
    letter-spacing: 0.2px;
  }
  .seascape {
    position: relative;
    flex: 1;
    background: linear-gradient(180deg,
      var(--sky-light) 0%,
      var(--sky) 40%,
      var(--sea-light) 47%,
      var(--sea) 62%,
      var(--sea-deep) 80%,
      var(--sea-dark) 100%);
  }
  .target {
    position: absolute;
    width: 54px;
    height: 54px;
    transform: translate(-50%, -50%);
  }
</style>
</head>
<body>
  <main class="wall">
    <section class="panel">
      <header class="panel-header">
        <div class="brand">
          <span class="brand-mark"></span>
          <span class="brand-name">Verdant Crest</span>
        </div>
      </header>
      <div class="seascape" role="img" aria-label="Open sea with rolling blue waves under a pale sky">
        <svg class="target" style="left:81px; top:204px" viewBox="0 0 54 54" aria-hidden="true">
          <circle cx="27" cy="27" r="17" fill="none" stroke="#fff" stroke-width="1.5"/>
          <line x1="0" y1="27" x2="54" y2="27" stroke="#fff" stroke-width="1"/>
          <line x1="27" y1="0" x2="27" y2="54" stroke="#fff" stroke-width="1"/>
          <circle cx="27" cy="27" r="9" fill="#fff"/>
        </svg>
      </div>
    </section>

    <section class="panel">
      <header class="panel-header"><h2 class="keyword">Sovereign<br>Solutions</h2></header>
      <div class="seascape" role="img" aria-label="Open sea with rolling blue waves under a pale sky"></div>
    </section>

    <section class="panel">
      <header class="panel-header"><h2 class="keyword">Deployable</h2></header>
      <div class="seascape" role="img" aria-label="Open sea with rolling blue waves and sea spray on the horizon"></div>
    </section>

    <section class="panel">
      <header class="panel-header"><h2 class="keyword">Underwater</h2></header>
      <div class="seascape" role="img" aria-label="Open sea with rolling blue waves under a pale sky"></div>
    </section>

    <section class="panel">
      <header class="panel-header"><h2 class="keyword">On Water</h2></header>
      <div class="seascape" role="img" aria-label="Open sea with rolling blue waves under a pale sky">
        <svg class="target" style="left:87px; top:204px" viewBox="0 0 54 54" aria-hidden="true">
          <circle cx="27" cy="27" r="17" fill="none" stroke="#fff" stroke-width="1.5"/>
          <line x1="0" y1="27" x2="54" y2="27" stroke="#fff" stroke-width="1"/>
          <line x1="27" y1="0" x2="27" y2="54" stroke="#fff" stroke-width="1"/>
          <circle cx="27" cy="27" r="9" fill="#fff"/>
        </svg>
      </div>
    </section>

    <section class="panel">
      <header class="panel-header"><h2 class="keyword">Above Water</h2></header>
      <div class="seascape" role="img" aria-label="Open sea with breaking waves under a pale sky">
        <svg class="target" style="left:82px; top:33px" viewBox="0 0 54 54" aria-hidden="true">
          <circle cx="27" cy="27" r="17" fill="none" stroke="#fff" stroke-width="1.5"/>
          <line x1="0" y1="27" x2="54" y2="27" stroke="#fff" stroke-width="1"/>
          <line x1="27" y1="0" x2="27" y2="54" stroke="#fff" stroke-width="1"/>
          <circle cx="27" cy="27" r="9" fill="#fff"/>
        </svg>
      </div>
    </section>
  </main>
</body>
</html>
```